CalmPeak Nurses' Manifesto

Design a manifesto to inspire and motivate nurses to work at minimum standards of excellence in their nursing practice.

The manifesto will become a feature of our website, at conferences, workshops and retreats. It will also be featured on other marketing tools.

Primary Market:
Nurses and/or other healthcare professionals (specifically Doctors, Occupational Therapists, Psychologists and Social Workers).

However the manifesto is equally applicable to all nurses and healthcare professionals from new graduates to very experienced senior clinicians, administration officers,managers and healthcare executive personnel.

Mainly females and primarily 35 to 65 years old, which suggests people in this target age group have extensive experience, but have become jaded'.

The purpose of our business is to assist healthcare professionals, primarily nurses, to maintain their enthusiasm and excellence in service provision, for their benefit as well as the benefit of the clients.

I have attached:
File 1: Copy Samples and examples: which has the copy for the manifesto, examples that appeal to us and our 3 attempts.
File 2: Our colour Spec Sheet, HOWEVER the colours are not necessary limited to these colours. These colours are not in the logo that will be on the manifesto. The colours on the logo attached can/or also be used.
File 3: Prototype logo. The final logo will be available within 3 to 4 days.

Industry/Entity Type

Healthcare

Requirements
Must have
• Must use the copy as per the attached file.

It should be contemporary, eye catching and motivational.

Should not have
• MUST BE EASY TO READ. Each line MUST be clearly defined from each other.

```html
<!DOCTYPE html>
<html lang="en">
<head>
<meta charset="utf-8">
<title>CalmPeak Nurses' Manifesto</title>
<link href="https://fonts.googleapis.com/css2?family=League+Gothic&family=Kaushan+Script&family=Delius&family=Ubuntu:wght@500;700&family=Pinyon+Script&family=Montserrat:wght@700;800&family=Caveat+Brush&family=Quicksand:wght@500;600&family=Caveat:wght@500&family=Nunito:ital,wght@1,800;1,900&family=Exo+2:ital,wght@0,500;1,900&family=Didact+Gothic&display=swap" rel="stylesheet">
<style>
  :root {
    --leaf: #7fab55;
    --sage: #6e9c5f;
    --fern: #64967a;
    --moss: #558a6c;
    --pine: #3f6f58;
    --forest: #2f5a49;
    --paper: #ffffff;
  }
  * { margin: 0; padding: 0; box-sizing: border-box; }
  html, body { width: 1200px; height: 1000px; overflow: hidden; background: var(--paper); }
  .manifesto { position: relative; width: 1200px; height: 1000px; overflow: hidden; background: var(--paper); }
  .line { position: absolute; white-space: nowrap; line-height: 1; font-weight: normal; }

  .headline { left: 12px; top: 4px; font-family: "League Gothic", sans-serif; font-size: 112px; color: var(--leaf); transform: scaleX(0.87); transform-origin: left top; }
  .headline .small { font-size: 60px; }

  .self-care { font-family: "Kaushan Script", cursive; font-size: 33px; color: var(--leaf); }
  .delight { font-family: "Delius", cursive; font-size: 37px; color: var(--leaf); letter-spacing: 1px; }
  .delight .big { font-size: 43px; }
  .delight .care { font-family: "Kaushan Script", cursive; font-size: 44px; }
  .delight .deliver { font-family: "Kaushan Script", cursive; }

  .respect { font-family: "Ubuntu", sans-serif; font-weight: 500; font-size: 24px; color: var(--sage); }
  .respect b { font-weight: 700; font-size: 37px; }

  .support { font-family: "Pinyon Script", cursive; font-size: 56px; color: var(--sage); }
  .learn { font-family: "Montserrat", sans-serif; font-weight: 800; font-size: 23px; color: var(--sage); letter-spacing: 1px; }
  .learn .big { font-size: 37px; }
  .lifelong { font-family: "Pinyon Script", cursive; font-size: 64px; color: var(--sage); }

  .trust { font-family: "Caveat Brush", cursive; font-size: 39px; color: var(--fern); letter-spacing: 1px; }
  .trust .big { font-size: 47px; }

  .smile { font-family: "Quicksand", sans-serif; font-weight: 500; font-size: 28px; color: var(--fern); }
  .smile .big { font-family: "Caveat Brush", cursive; font-size: 42px; }

  .diversity { left: 385px; font-family: "League Gothic", sans-serif; font-size: 44px; color: var(--fern); letter-spacing: 0.5px; transform: scaleX(0.9); transform-origin: left top; }
  .diversity .big { font-size: 78px; }

  .right-thing { font-family: "Kaushan Script", cursive; font-size: 35px; color: var(--fern); letter-spacing: 1px; }
  .solution { font-family: "Kaushan Script", cursive; font-size: 34px; color: var(--moss); }
  .unique { font-family: "Caveat", cursive; font-weight: 500; font-size: 58px; color: var(--moss); }

  .leaders { font-family: "Nunito", sans-serif; font-style: italic; font-weight: 800; font-size: 30px; color: var(--moss); }
  .seek { font-family: "Exo 2", sans-serif; font-weight: 500; font-size: 29px; color: var(--moss); letter-spacing: 2.5px; }
  .lead-purpose { font-family: "Didact Gothic", sans-serif; font-size: 38px; color: var(--pine); }
  .respond { font-family: "Pinyon Script", cursive; font-size: 36px; color: var(--pine); }
  .respond.small { font-size: 33px; }
  .choose { font-family: "Nunito", sans-serif; font-style: italic; font-weight: 900; font-size: 24px; color: var(--pine); }
  .choose .big { font-size: 31px; }
  .adopt { font-family: "Ubuntu", sans-serif; font-weight: 700; font-size: 21px; color: var(--forest); }
  .adopt .big { font-size: 24px; }
  .dream { font-family: "Exo 2", sans-serif; font-style: italic; font-weight: 900; font-size: 72px; color: var(--forest); }

  .brand { position: absolute; left: 770px; top: 905px; display: flex; align-items: center; gap: 16px; }
  .brand-mark { width: 56px; height: 56px; background: var(--fern); }
  .brand-name { font-family: "Quicksand", sans-serif; font-weight: 600; font-size: 34px; color: var(--forest); }
</style>
</head>
<body>
<main class="manifesto">
  <h1 class="line headline">NURSE <span class="small">WITH</span> OPEN HANDS, HEARTS <span class="small">AND</span> MINDS.</h1>

  <p class="line self-care" style="left:8px; top:100px;">Look after yourself and value your health as much as you value the</p>
  <p class="line self-care" style="left:8px; top:160px;">health of others.</p>

  <p class="line delight" style="left:236px; top:140px;"><span class="big">Delight</span> your <span class="big">clients</span> and <span class="big">colleagues</span> by exceeding</p>
  <p class="line delight" style="left:236px; top:190px;">their <span class="big">expectations.</span> <span class="deliver">Deliver <span class="care">care</span> skillfully.</span></p>

  <p class="line respect" style="left:32px; top:238px;"><b>Respect</b> the limits of <b>people's knowledge</b> and share your knowledge <b>generously.</b></p>

  <p class="line support" style="left:12px; top:282px;">Support your colleagues</p>
  <p class="line learn" style="left:520px; top:293px;">LEARN <span class="big">SOMETHING NEW</span> EACH DAY.</p>
  <p class="line support" style="left:12px; top:366px; font-size:48px;">and champion their purpose.</p>
  <p class="line lifelong" style="left:562px; top:336px;">Be a lifelong learner.</p>

  <p class="line trust" style="left:40px; top:418px;">Trust your <span class="big">knowledge</span> and seek <span class="big">advice</span> only from respected sources.</p>

  <p class="line smile" style="left:12px; top:490px;"><span class="big">Smile</span> and <span class="big">infect</span> others</p>
  <p class="line smile" style="left:12px; top:540px;">with your <span class="big">happiness</span></p>
  <p class="line smile" style="left:12px; top:590px;">and have <span class="big">fun</span> !</p>

  <p class="line diversity" style="top:478px;">CELEBRATE, <span class="big">RESPECT</span> AND VALUE THE <span class="big">DIVERSITY</span> OF</p>
  <p class="line diversity" style="top:540px;"><span class="big">AUSTRALIAN</span> CULTURE.</p>

  <p class="line right-thing" style="left:775px; top:558px;">Always do the right</p>
  <p class="line right-thing" style="left:768px; top:618px;">thing without exception.</p>

  <p class="line solution" style="left:5px; top:638px;">Always be solution</p>
  <p class="line solution" style="left:20px; top:700px;">focused.</p>

  <p class="line unique" style="left:315px; top:614px;">You are unique, revel</p>
  <p class="line unique" style="left:178px; top:680px;">in your individuality.</p>

  <p class="line leaders" style="left:652px; top:678px;">Only follow exceptional leaders.</p>
  <p class="line leaders" style="left:572px; top:724px;">If there is no one left to follow, then lead!</p>

  <p class="line seek" style="left:8px; top:758px;">Seek success firstly from within.</p>
  <p class="line lead-purpose" style="left:12px; top:793px;">Always lead with purpose,</p>
  <p class="line lead-purpose" style="left:12px; top:833px;">passion and commitment.</p>

  <p class="line respond" style="left:582px; top:758px;">Respond to complex situations innovatively,</p>
  <p class="line respond small" style="left:470px; top:814px;">creatively and safely within the scope of your practice.</p>

  <p class="line choose" style="left:460px; top:852px;"><span class="big">Choose</span> your thoughts <span class="big">wisely</span>, they create your <span class="big">reality</span>.</p>

  <p class="line adopt" style="left:8px; top:877px;"><span class="big">Adopt</span> a 'can do' <span class="big">attitude</span> to everything</p>
  <p class="line adopt" style="left:8px; top:904px;">that comes your way.</p>

  <p class="line dream" style="left:10px; top:924px;">Live your dream.</p>

  <div class="brand">
    <span class="brand-mark"></span>
    <span class="brand-name">CalmPeak</span>
  </div>
</main>
</body>
</html>
```